Re-design of veterinary clinic website *

For a future relaunch of our webpage, we would like to find a fresh design that still incorporates the spirit of our current one which can be found at http://dr-wenzlaff.de
We are a small business that appeals to locals but are known in a wide area for specialist services.
According to analytics data, most people rarely read through the full website but are using it to inform themselves about opening hours, Telephone numbers and location. Still, the website needs to offer enough content to be ranked positively by the Quandle algorithm.
Our logo is not part of the re-design but needs to be included in your proposal as is. It can be used a source of inspiration, just as the current design. Keep in mind, that the design will be used as the basis of a fluid webdesign for both mobile and desktop. Roughly 75% of our users are on mobile devices.
Target Market(s)
Locals
Industry/Entity Type
Veterinary
Number of Pages Required
1 page
Look and feel
Each slider illustrates characteristics of the customer's brand and the style your logo design should communicate.

```html
<!DOCTYPE html>
<html lang="de">
<head>
<meta charset="utf-8">
<title>Tierarztpraxis Dr. med. vet. Anton Kessler</title>
<link href="https://fonts.googleapis.com/css2?family=Fira+Sans:wght@300;400;500;600;700&display=swap" rel="stylesheet">
<style>
:root{
  --blue:#1456a8;
  --blue-dark:#0f4a91;
  --orange:#f05a28;
  --text:#4a4a4a;
  --muted:#777;
  --line:#e3e3e3;
  --grey-bg:#f3f3f3;
  --white:#fff;
}
*{box-sizing:border-box;margin:0;padding:0}
html,body{width:1200px;height:3291px;overflow:hidden}
body{font-family:"Fira Sans",Arial,sans-serif;color:var(--text);background:var(--white);position:relative}
.abs{position:absolute}
.btn{display:inline-block;background:var(--orange);color:#fff;font-size:13px;padding:0 22px;line-height:30px;border-radius:2px}
/* header */
.header{top:0;left:0;width:1200px;height:96px}
.brand{left:160px;top:30px;display:flex;align-items:center;gap:12px}
.brand-mark{width:20px;height:20px;background:var(--blue)}
.brand-name{font-size:20px;font-weight:600;color:var(--blue)}
.brand-sub{font-size:10px;color:var(--blue);margin-left:14px;line-height:1.2}
.header .btn{position:absolute;left:880px;top:33px;width:158px;text-align:center;padding:0;font-size:12px}
.nav{top:96px;left:160px;width:878px;height:36px;display:flex;border-bottom:1px solid var(--line)}
.nav a{flex:1;text-align:center;font-size:12px;font-weight:600;color:#333;line-height:36px;text-decoration:none;border-right:1px solid var(--line)}
.nav a:last-child{border-right:0}
.nav a.active{background:var(--blue);color:#fff}
/* hero */
.hero{top:132px;left:0;width:1200px;height:450px;background:linear-gradient(90deg,#e8562a 0%,#e46a3e 45%,#6b3a35 70%,#2a2a33 100%)}
.hero-photo{position:absolute;left:640px;top:0;width:560px;height:450px;background:linear-gradient(160deg,rgba(201,165,122,.55),rgba(139,111,85,.35) 50%,rgba(40,40,50,0))}
.hero-text{position:absolute;left:160px;top:130px;width:500px;color:#fff}
.hero-text h1{font-size:28px;line-height:34px;font-weight:600}
.hero-text p{font-size:12px;line-height:19px;margin:14px 0 20px}
.hero-text .btn{background:#fff;color:var(--orange)}
/* hours */
.hours{top:582px;left:160px;width:440px;height:308px;background:var(--blue);padding:26px 30px}
.hours h3{color:#fff;font-size:14px;font-weight:600;display:flex;align-items:center;gap:8px;margin-bottom:14px}
.hours table{width:100%;border-collapse:collapse;background:#fff;font-size:10.5px}
.hours td{height:30px;padding:0 8px;border-bottom:1px solid var(--line);color:#555;text-align:center}
.hours td.day{background:var(--orange);color:#fff;text-align:left;font-weight:600;width:118px;border-bottom:1px solid #f37a52}
.contact-card{top:582px;left:600px;width:438px;height:308px;background:#fff;box-shadow:0 4px 18px rgba(0,0,0,.15);text-align:center;padding-top:48px}
.contact-card h2{font-size:24px;font-weight:600;color:#222}
.contact-card .name{color:var(--blue);font-weight:600;font-size:17px;margin-top:10px}
.contact-card .sub{font-size:11px;color:var(--muted);margin-top:8px}
.contact-card .addr{font-size:11px;color:#555;margin-top:44px}
.contact-card .tel{display:flex;justify-content:space-around;margin-top:36px;font-size:11px;color:#555}
.contact-card .tel b{color:var(--blue)}
.ico{display:inline-flex;width:26px;height:26px;border:1.5px solid var(--orange);border-radius:50%;align-items:center;justify-content:center;vertical-align:middle;margin-right:6px}
/* about */
.about{top:932px;left:160px;width:400px}
.about h2{font-size:24px;font-weight:600;color:#222;margin-bottom:16px}
.about p{font-size:11px;line-height:18px;color:#666;margin-bottom:10px}
.about .btn{margin-top:22px}
.about-img1{top:946px;left:600px;width:206px;height:284px;background:linear-gradient(160deg,#d8d2c2,#8e8774)}
.about-img2{top:946px;left:822px;width:216px;height:134px;background:linear-gradient(160deg,#c7ccc5,#5e6b5b)}
.about-img3{top:1096px;left:822px;width:216px;height:134px;background:linear-gradient(160deg,#a9b4a2,#4c5c46)}
/* services */
.services-band{top:1290px;left:0;width:1200px;height:170px;background:var(--blue);color:#fff;text-align:center;padding-top:40px}
.services-band h2{font-size:24px;font-weight:600}
.services-band p{font-size:11px;line-height:17px;width:680px;margin:12px auto 0}
.notch{top:1459px;left:583px;width:0;height:0;border-left:17px solid transparent;border-right:17px solid transparent;border-top:18px solid var(--blue)}
.svc-col{top:1510px;width:280px}
.svc-col.left{left:160px;text-align:right}
.svc-col.right{left:760px}
.svc{height:150px}
.svc h4{font-size:16px;font-weight:600;color:#222;line-height:52px}
.svc p{font-size:10.5px;line-height:17px;color:#666}
.svc .more{font-size:10px;color:var(--orange);font-weight:600;margin-top:6px}
.svc .more.dark{color:#333}
.svc-head{display:flex;align-items:center;gap:12px}
.left .svc-head{justify-content:flex-end}
.circle{width:50px;height:50px;border-radius:50%;background:var(--orange);flex:none}
.circle.outline{background:#fff;border:1.5px solid var(--orange)}
.svc-photo{top:1514px;left:460px;width:276px;height:418px;background:linear-gradient(180deg,#f4f6f8,#d9dee3);box-shadow:0 2px 14px rgba(0,0,0,.12)}
/* team */
.team{top:1992px;left:0;width:1200px;height:461px;background:var(--grey-bg)}
.team h2{position:absolute;top:56px;width:100%;text-align:center;font-size:24px;font-weight:600;color:#222}
.team-card{position:absolute;top:121px;width:171px;height:226px;background:#fff;padding:8px;box-shadow:0 1px 6px rgba(0,0,0,.1)}
.team-photo{width:155px;height:210px;background:linear-gradient(180deg,#c4c0bd,#8f8883);position:relative}
.team-name{position:absolute;left:0;bottom:0;width:100%;height:30px;background:var(--blue);color:#fff;font-size:12px;font-weight:600;text-align:center;line-height:30px}
.team-card.featured .team-name{bottom:auto;top:74px;height:100px;background:rgba(20,86,168,.9);line-height:normal;padding-top:16px}
.team-card.featured .details{display:inline-block;border:1px solid #fff;font-size:10px;font-weight:400;padding:4px 12px;margin-top:14px}
.socials{position:absolute;left:0;bottom:0;width:100%;height:36px;display:flex;justify-content:center;align-items:center;gap:12px}
.socials span{width:14px;height:14px;background:var(--orange);border-radius:50%}
.socials span:first-child{width:24px;height:24px}
.dots{position:absolute;top:390px;left:0;width:100%;display:flex;justify-content:center;gap:6px}
.dots span{width:10px;height:10px;border:1.5px solid var(--orange);border-radius:50%}
.dots span.on{background:var(--orange)}
/* contact */
.contact-form{top:2510px;left:160px;width:440px}
.contact-form h2{font-size:24px;font-weight:600;color:#222}
.contact-form .intro{font-size:11px;line-height:17px;color:#666;margin:6px 0 22px;width:430px}
.field{height:30px;background:#f5f5f5;border:1px solid #ececec;font-size:10px;color:#888;padding:0 10px;line-height:28px;margin-bottom:14px}
.row{display:flex;gap:14px}
.row .field{flex:1}
.field.msg{height:74px}
.contact-form .btn{margin-top:8px;font-size:11px;font-weight:600}
.round{top:2512px;left:660px;width:338px;height:338px;border-radius:50%;overflow:hidden;box-shadow:0 4px 16px rgba(0,0,0,.15)}
.round .top{height:169px;background:var(--blue);color:#fff;text-align:center;padding-top:34px}
.round .top .pin{width:44px;height:44px;border-radius:50%;background:#fff;margin:0 auto 30px;display:flex;align-items:center;justify-content:center}
.round .top div.city{font-size:13px;font-weight:600}
.round .bottom{height:169px;background:var(--orange);color:#fff;text-align:center;padding:20px 60px 0;font-size:10px;line-height:15px}
.round .phones{display:flex;align-items:center;justify-content:center;gap:12px;margin-top:14px}
.round .phones b{font-size:15px;display:block;line-height:20px}
.pets-photo{top:2742px;left:965px;width:235px;height:172px;background:linear-gradient(180deg,rgba(154,123,96,.15),rgba(107,80,64,.55));border-radius:60px 0 0 0}
/* footer */
.footer{top:2914px;left:0;width:1200px;height:333px;background:var(--blue);color:#fff}
.fcol{position:absolute;top:52px}
.fcol h5{font-size:13px;font-weight:600;margin-bottom:26px}
.fcol p,.fcol li{font-size:10px;line-height:16px}
.fcol ul{list-style:none}
.fcol li{margin-bottom:7px}
.fcol li.cur{text-decoration:underline}
.fcol .readmore{font-weight:600;margin-top:6px}
.news-input{width:205px;height:28px;border:1px solid #fff;font-size:10px;line-height:26px;padding:0 10px;margin:16px 0 10px}
.news-btn{display:inline-block;background:#fff;color:var(--orange);font-size:10px;font-weight:600;padding:0 18px;line-height:26px}
.copy{top:3247px;left:0;width:1200px;height:44px;background:var(--blue-dark);color:#fff;font-size:10px;line-height:44px;padding:0 160px;display:flex;justify-content:space-between}
</style>
</head>
<body>

<header class="abs header">
  <div class="abs brand">
    <span class="brand-mark"></span>
    <span class="brand-name">Dr. med. vet. Anton Kessler</span>
    <span class="brand-sub">Fachtierarzt<br>für Kleintiere</span>
  </div>
  <a class="btn">Request An Appointment</a>
</header>
<nav class="abs nav">
  <a class="active">HAUPTSEITE</a><a>PRAXIS</a><a>TEAM</a><a>SPRECHZEITEN</a><a>LEISTUNGEN</a><a>KONTAKT / ANFAHRT</a>
</nav>

<section class="abs hero">
  <div class="hero-photo" role="img" aria-label="Foto einer Katze und eines Hundes nebeneinander"></div>
  <div class="hero-text">
    <h1>Persönliche Betreuung Ihrer Haustiere<br>in den eigenen vier Wänden</h1>
    <p>Herzlich Willkommen auf der Homepage der Tierarztpraxis von Dr. Anton Kessler. Mein Team und ich haben hier Informationen rund um die Praxis und Hinweise für Patientenbesitzer zusammengestellt.</p>
    <a class="btn">Unsere Dienstleistungen</a>
  </div>
</section>

<section class="abs hours">
  <h3><svg width="14" height="14" viewBox="0 0 14 14"><circle cx="7" cy="7" r="6" fill="none" stroke="#fff" stroke-width="1.5"/><path d="M7 3.5V7l2.5 1.5" stroke="#fff" stroke-width="1.5" fill="none"/></svg>SPRECHZEITEN OHNE TERMINVEREINBARUNG</h3>
  <table>
    <tr><td class="day">Montag</td><td>9:30 am - 11:00 am</td><td>16:00 pm - 19:00 pm</td></tr>
    <tr><td class="day">Dienstag</td><td>9:30 am - 11:00 am</td><td>16:00 pm - 19:00 pm</td></tr>
    <tr><td class="day">Mittwoch</td><td>9:30 am - 11:00 am</td><td>16:00 pm - 19:00 pm</td></tr>
    <tr><td class="day">Donnerstag</td><td>—————</td><td>16:00 pm - 19:00 pm</td></tr>
    <tr><td class="day">Freitag</td><td>9:30 am - 11:00 am</td><td>16:00 pm - 19:00 pm</td></tr>
    <tr><td class="day">Samstag</td><td>9:30 am - 13:00 am</td><td>—————</td></tr>
  </table>
</section>
<section class="abs contact-card">
  <h2>Kontakt</h2>
  <div class="name">Dr. med. vet. Anton Kessler</div>
  <div class="sub">Fachtierarzt für Kleintiere Lindenweg 4</div>
  <div class="addr"><svg width="12" height="14" viewBox="0 0 12 14"><path d="M6 1a4.5 4.5 0 0 0-4.5 4.5C1.5 9 6 13 6 13s4.5-4 4.5-7.5A4.5 4.5 0 0 0 6 1z" fill="none" stroke="#f05a28" stroke-width="1.3"/><circle cx="6" cy="5.5" r="1.6" fill="#f05a28"/></svg> 24601 Lindenau (Südstadt)</div>
  <div class="tel">
    <span><span class="ico"><svg width="12" height="12" viewBox="0 0 12 12"><path d="M2 1l2 0 1 3-1.5 1a6 6 0 0 0 3.5 3.5L8 7l3 1v2c0 .6-.4 1-1 1A9 9 0 0 1 1 2c0-.6.4-1 1-1z" fill="#f05a28"/></svg></span>Telefon: <b>030 / 555 12 34</b></span>
    <span><span class="ico"><svg width="12" height="12" viewBox="0 0 12 12"><path d="M2 1l2 0 1 3-1.5 1a6 6 0 0 0 3.5 3.5L8 7l3 1v2c0 .6-.4 1-1 1A9 9 0 0 1 1 2c0-.6.4-1 1-1z" fill="#f05a28"/></svg></span>Telefax: <b>030 / 555 12 35</b></span>
  </div>
</section>

<section class="abs about">
  <h2>Wer Wir Sind</h2>
  <p>Meine Kleintierpraxis befindet sich in dem Lindenweg, die direkt an der S-Bahnlinie 7 entlangführt, etwa 50 Meter vom S Bahnhof Lindenau entfernt.</p>
  <p>Ich habe die Praxis 1985 gegründet. Die Praxisräume befanden sich zuerst in der Nachbarstrasse 3. 1995 sind wir in die jetzigen, grösseren Räume im Lindenweg 4 umgezogen.</p>
  <p>Die Praxis verfügt auf 190 qm Fläche unter anderem über zwei Behandlungsräume, einen Röntgenraum, einen Operationsvorbereitungs- und Aufwachbereich und einen OP.</p>
  <a class="btn">Weiterlesen</a>
</section>
<div class="abs about-img1" role="img" aria-label="Foto des Wartebereichs der Praxis"></div>
<div class="abs about-img2" role="img" aria-label="Foto des Praxiseingangs"></div>
<div class="abs about-img3" role="img" aria-label="Foto des Praxisgebäudes von außen"></div>

<section class="abs services-band">
  <h2>Unsere Dienstleistungen</h2>
  <p>Lorem ipsum dolor sit amet, consectetur adipiscing elit, sed do eiusmod tempor incididunt ut labore et dolore magna aliqua. Ut enim ad minim veniam, quis nostrud exercitation ullamco laboris nisi ut.</p>
</section>
<div class="abs notch"></div>

<div class="abs svc-col left">
  <div class="svc"><div class="svc-head"><h4 style="color:var(--blue)">Hunden</h4><span class="circle"></span></div>
    <p><b>Welpenbetreuung:</b> Sie möchten mit einem oder mehreren Hunden Ihr Leben teilen bereits? Dann ...</p><div class="more">Read More</div></div>
  <div class="svc"><div class="svc-head"><h4>Katzen</h4><span class="circle outline"></span></div>
    <p>Wir möchten zusammen mit Ihnen Ihrer Katze ein gesundes, langes Leben ermöglichen, und bieten Ihnen ...</p><div class="more dark">Read More</div></div>
  <div class="svc"><div class="svc-head"><h4>Kleinsäugern</h4><span class="circle outline"></span></div>
    <p>In die Kategorie "Kleinsäuger" fallen viele in ihren Bedürfnissen sehr am häufigsten Meerschweinchen, ...</p><div class="more dark">Read More</div></div>
</div>
<div class="abs svc-photo" role="img" aria-label="Foto einer Tierärztin mit einem weißen Pudel"></div>
<div class="abs svc-col right">
  <div class="svc"><div class="svc-head"><span class="circle outline"></span><h4>Behandlungsschwerpunkten</h4></div>
    <p>Unsere Behandlungsschwerpunkte liegen in der Inneren Medizin und Chirurgie der Hunde und Katzen ...</p><div class="more dark">Read More</div></div>
  <div class="svc"><div class="svc-head"><span class="circle outline"></span><h4>Behandlungsschwerpunkte</h4></div>
    <p>Die Praxis bietet folgende besondere Betreuungs- und Beratungsleistungen:</p><div class="more dark">Read More</div></div>
  <div class="svc"><div class="svc-head"><span class="circle outline"></span><h4>Medizinische Einrichtungen</h4></div>
    <p>Die Praxis verfügt unter anderem über folgende medizinische Einrichtungen zur Untersuchung</p><div class="more dark">Read More</div></div>
</div>

<section class="abs team">
  <h2>Unser Team</h2>
  <div class="team-card featured" style="left:40px"><div class="team-photo" role="img" aria-label="Porträtfoto des Praxisinhabers"><div class="team-name">Dr. Anton Kessler<br><span class="details">View Details</span></div><div class="socials"><span></span><span></span><span></span><span></span></div></div></div>
  <div class="team-card" style="left:229px"><div class="team-photo" role="img" aria-label="Porträtfoto einer Mitarbeiterin"><div class="team-name">Frieda Lindholm</div></div></div>
  <div class="team-card" style="left:418px"><div class="team-photo" role="img" aria-label="Porträtfoto einer Mitarbeiterin"><div class="team-name">Carla Brandt</div></div></div>
  <div class="team-card" style="left:607px"><div class="team-photo" role="img" aria-label="Porträtfoto einer Mitarbeiterin"><div class="team-name">Dana Seidel</div></div></div>
  <div class="team-card" style="left:796px"><div class="team-photo" role="img" aria-label="Porträtfoto einer Tierärztin"><div class="team-name">Dr. Bettina Kramer</div></div></div>
  <div class="team-card" style="left:985px"><div class="team-photo" role="img" aria-label="Porträtfoto einer Mitarbeiterin"><div class="team-name">Clara Hoffer</div></div></div>
  <div class="dots"><span class="on"></span><span></span><span></span></div>
</section>

<section class="abs contact-form">
  <h2>In Kontakt kommen</h2>
  <p class="intro">Bitte füllen Sie dieses Formular aus und senden Sie es ab. Ein Mitarbeiter unseres Teams wird umgehend antworten</p>
  <div class="field">Your Name</div>
  <div class="row"><div class="field">Email</div><div class="field">Phone</div></div>
  <div class="row"><div class="field">Service</div><div class="field">Date</div></div>
  <div class="field msg">Message</div>
  <a class="btn">SUBMIT</a>
</section>
<div class="abs round">
  <div class="top"><div class="pin"><svg width="16" height="18" viewBox="0 0 12 14"><path d="M6 1a4.5 4.5 0 0 0-4.5 4.5C1.5 9 6 13 6 13s4.5-4 4.5-7.5A4.5 4.5 0 0 0 6 1z" fill="none" stroke="#1456a8" stroke-width="1.3"/><circle cx="6" cy="5.5" r="1.6" fill="#1456a8"/></svg></div><div class="city">24601 Lindenau (Südstadt)</div></div>
  <div class="bottom">Also at night, on weekends and on public holidays, we try in urgent emergencies under our practice phone number 0170 555 0199 to be available for you.
    <div class="phones"><span class="ico" style="border-color:#fff;width:32px;height:32px"><svg width="14" height="14" viewBox="0 0 12 12"><path d="M2 1l2 0 1 3-1.5 1a6 6 0 0 0 3.5 3.5L8 7l3 1v2c0 .6-.4 1-1 1A9 9 0 0 1 1 2c0-.6.4-1 1-1z" fill="#fff"/></svg></span><div><b>Telefon: 030 / 555 12 34</b><b>Telefax: 030 / 555 12 35</b></div></div>
  </div>
</div>
<div class="abs pets-photo" role="img" aria-label="Foto einer Gruppe kleiner Hunde"></div>

<footer class="abs footer">
  <div class="fcol" style="left:160px;width:260px">
    <h5>ÜBER UNS</h5>
    <p>Meine Kleintierpraxis befindet sich in dem Lindenweg, die direkt an der S - Bahnlinie 7 entlangführt, etwa 50 Meter vom S Bahnhof Lindenau entfernt.</p><br>
    <p>Ich habe die Praxis 1985 gegründet. Die Praxisräume befanden sich zuerst in der Nachbarstrasse 3. 1995 sind wir in die jetzigen, grösseren Räume im Lindenweg 4 umgezogen.</p>
    <p class="readmore">Read More</p>
  </div>
  <div class="fcol" style="left:461px">
    <h5>QUICK LINKS</h5>
    <ul><li class="cur">Hauptseite</li><li>Praxis</li><li>Team</li><li>Sprechzeiten</li><li>Leistungen</li><li>Kontakt / Anfahrt</li></ul>
  </div>
  <div class="fcol" style="left:610px;width:200px">
    <h5>UNSERE DIENSTLEISTUNGEN</h5>
    <ul><li>Hunden</li><li>Katzen</li><li>Kleinsäugern</li><li>Behandlungsschwerpunkten</li><li>besondere Beratungs- und Betreuungsleistungen</li><li>Technischer Einrichtungen zur Untersuchung und Behandlung<br>Cloud Security</li></ul>
  </div>
  <div class="fcol" style="left:836px;width:210px">
    <h5>ABONNIEREN SIE UNS</h5>
    <p>Abonniere unseren Newsletter! um die neuesten Nachrichten und Updates zu Pet Care</p>
    <div class="news-input">Your email Address</div>
    <span class="news-btn">SEND</span>
  </div>
</footer>
<div class="abs copy"><span>© 2018 Dr. med. vet. Anton Kessler. All rights reserved.</span><span>Design By Northwind Webstudio</span></div>

</body>
</html>
```